Harwell Properties Business Cards

I would like a business card that includes myself and my partner.
Includes: Logo, office #, email, website, our names, our numbers and possibly the address. I would also like the logo to be embossed and the card to be horizontal.
There is a photo of our yard signs to give you an idea of the colors of our business.

Target Market(s)

Everyone in real estate market.
We are in a rural area. Our clientele are from all socioeconomic backgrounds.

Industry/Entity Type

Real Estate Agent

Contact Information for Business Card

Company Name: Harwell Properties
Our Names, Titles & Cell #'s : Dana Harwell-Broker (555).613.2947, Marla Harwell-Realtor (555).730.5816
Office #: (555).264.1300
Website: harwellproperties.example
Joint Email: harwell@harwellproperties.example
Office Address: 418C W. Pell Creek St.
Brazoria, TX. 00518

Font styles to use
Serif

Requirements
Must have
• HORIZONTAL, Logo, Myself and my partners names, Our cell #'s, our office #, our website, our email address
Nice to have
• Embossed logo, office address, our titles.

```html
<!DOCTYPE html>
<html lang="en">
<head>
<meta charset="utf-8">
<title>Harwell Properties Business Cards</title>
<link rel="stylesheet" href="https://fonts.googleapis.com/css2?family=Cinzel:wght@400;700&family=Open+Sans:wght@400&display=swap">
<style>
  :root {
    --stage: #4a4a4c;
    --plum: #4f2f56;
    --plum-light: #6b4478;
    --plum-dark: #3e2345;
    --olive: #3d441f;
    --cream: #f3ecce;
    --gold: #e9d9a6;
    --white: #f7f4f0;
  }
  * { box-sizing: border-box; margin: 0; padding: 0; }
  html, body { width: 1200px; height: 980px; overflow: hidden; }
  body {
    background: var(--stage);
    font-family: "Cinzel", serif;
    position: relative;
  }
  .card {
    position: absolute;
    width: 700px;
    height: 400px;
    overflow: hidden;
    background: radial-gradient(ellipse at 60% 40%, var(--plum-light) 0%, var(--plum) 55%, var(--plum-dark) 100%);
  }
  .card--front { left: 60px; top: 50px; }
  .card--back { left: 440px; top: 500px; }

  .swoosh { position: absolute; inset: 0; width: 100%; height: 100%; }

  .brand {
    position: absolute;
    display: flex;
    align-items: center;
    gap: 16px;
    color: var(--white);
  }
  .brand__mark {
    flex: none;
    border-radius: 50%;
    background: var(--white);
  }
  .brand__name {
    font-family: "Cinzel", serif;
    font-weight: 700;
    letter-spacing: 1px;
    white-space: nowrap;
  }
  .card--front .brand { left: 50px; top: 60px; }
  .card--front .brand__mark { width: 46px; height: 46px; }
  .card--front .brand__name { font-size: 36px; }
  .card--back .brand { left: 0; right: 0; top: 165px; justify-content: center; gap: 20px; }
  .card--back .brand__mark { width: 62px; height: 62px; }
  .card--back .brand__name { font-size: 46px; }

  .partners { position: absolute; left: 50px; top: 175px; }
  .partner { margin-bottom: 16px; }
  .partner__name {
    color: var(--gold);
    font-size: 17px;
    letter-spacing: 0.5px;
  }
  .partner__role {
    color: var(--cream);
    font-size: 12px;
    letter-spacing: 1px;
    margin-top: 2px;
  }

  .divider {
    position: absolute;
    left: 300px; top: 150px;
    width: 1px; height: 130px;
    background: var(--cream);
  }

  .office {
    position: absolute;
    left: 316px; top: 150px;
    color: var(--cream);
    font-size: 11.5px;
    letter-spacing: 0.5px;
    line-height: 19px;
  }
  .office__address { margin-bottom: 12px; }
  .office__line { display: flex; align-items: center; gap: 7px; white-space: nowrap; }
  .office__line svg { width: 11px; height: 11px; flex: none; }

  .palette { position: absolute; left: 130px; top: 735px; }
  .palette__item { display: flex; align-items: center; gap: 35px; margin-bottom: 22px; }
  .palette__dot { width: 62px; height: 60px; border-radius: 50%; }
  .palette__code {
    font-family: "Open Sans", sans-serif;
    color: var(--white);
    font-size: 38px;
  }
</style>
</head>
<body>

<section class="card card--front" aria-label="Card front">
  <svg class="swoosh" viewBox="0 0 700 400" preserveAspectRatio="none" aria-hidden="true">
    <path d="M420 400 C 560 380, 630 300, 650 180 C 662 110, 680 60, 700 40 L700 400 Z" fill="var(--cream)"/>
    <path d="M470 400 C 600 385, 660 310, 672 200 C 682 130, 692 85, 700 70 L700 400 Z" fill="var(--olive)"/>
  </svg>

  <div class="brand">
    <span class="brand__mark" aria-hidden="true"></span>
    <span class="brand__name">Harwell Properties</span>
  </div>

  <div class="partners">
    <div class="partner">
      <div class="partner__name">Dana Harwell</div>
      <div class="partner__role">BROKER - (555).613.2947</div>
    </div>
    <div class="partner">
      <div class="partner__name">Marla Harwell</div>
      <div class="partner__role">REALTOR - (555).730.5816</div>
    </div>
  </div>

  <div class="divider"></div>

  <div class="office">
    <div class="office__address">418C W. PELL CREEK ST.<br>BRAZORIA, TX. 00518</div>
    <div class="office__line">
      <svg viewBox="0 0 12 12"><circle cx="6" cy="6" r="5.5" fill="var(--cream)"/><path d="M4 3.5 L5 3.5 L5.5 5 L4.8 5.6 Q5.6 7 6.5 7.3 L7 6.6 L8.5 7 L8.5 8 Q6 8.6 4 5 Z" fill="var(--plum)"/></svg>
      <span>(555).264.1300</span>
    </div>
    <div class="office__line">
      <svg viewBox="0 0 12 12"><circle cx="6" cy="6" r="5.5" fill="var(--cream)"/><path d="M0.5 6 H11.5 M6 0.5 V11.5 M2 3 H10 M2 9 H10" stroke="var(--plum)" stroke-width="0.7" fill="none"/></svg>
      <span>HARWELLPROPERTIES.EXAMPLE</span>
    </div>
    <div class="office__line">
      <svg viewBox="0 0 12 12"><rect x="0.5" y="2.5" width="11" height="7" fill="var(--cream)"/><path d="M0.5 2.5 L6 7 L11.5 2.5" stroke="var(--plum)" stroke-width="0.8" fill="none"/></svg>
      <span>HARWELL@HARWELLPROPERTIES.EXAMPLE</span>
    </div>
  </div>
</section>

<section class="card card--back" aria-label="Card back">
  <div class="brand">
    <span class="brand__mark" aria-hidden="true"></span>
    <span class="brand__name">Harwell Properties</span>
  </div>
</section>

<div class="palette" aria-label="Colour palette">
  <div class="palette__item"><span class="palette__dot" style="background: var(--olive)"></span><span class="palette__code">#3d441f</span></div>
  <div class="palette__item"><span class="palette__dot" style="background: var(--plum)"></span><span class="palette__code">#4f2f56</span></div>
  <div class="palette__item"><span class="palette__dot" style="background: var(--cream)"></span><span class="palette__code">#f3ecce</span></div>
</div>

</body>
</html>
```